GPS Tracker APP

Greetings,

We are looking for a UX designer to help us finalize the design of the Quelmo APP for iOS and Android. This is a GPS tracker app will be used by parents to track family cars or a small business with a fleet of vehicles. Its main benefits are family safety and fleet tracking.

We have created a pdf document (attached) with sample screens to show how the application should work. We also have a beta version available in the Pellux Store Kadro Store that we will provide so you can download and use for your reference. The app design should be up to par with the usability and design of wavo528 app, Other examples are: trelmo app and norvak gps app.

The designer must create and provide all the graphic assets so that our app developer can finalize the app.

```html
<!DOCTYPE html>
<html lang="en">
<head>
<meta charset="utf-8">
<title>Quelmo – GPS Tracker App Screens</title>
<link href="https://fonts.googleapis.com/css2?family=Open+Sans:wght@400;600;700;800&display=swap" rel="stylesheet">
<style>
  :root {
    --brand-blue: #1574b4;
    --brand-blue-dark: #0f5f99;
    --overlay-blue: rgba(110, 170, 210, 0.72);
    --card-bg: #dce9f3;
    --map-light: #f1f2f3;
    --map-mid: #e3e5e7;
    --ink: #222222;
    --ink-soft: #3a4a57;
    --danger: #e0404a;
    --accent-green: #5fd36a;
    --accent-purple: #6e5fd6;
    --accent-red: #ef3e5c;
    --page-bg: #ffffff;
    --frame: #eef2f6;
  }
  * { box-sizing: border-box; margin: 0; padding: 0; }
  html, body { width: 1200px; height: 1168px; overflow: hidden; background: var(--page-bg); }
  body { font-family: "Open Sans", sans-serif; color: var(--ink); position: relative; }

  .screen {
    position: absolute; top: 70px; width: 310px; height: 650px;
    border-radius: 40px; overflow: hidden;
    background: var(--frame); padding: 10px;
    box-shadow: 0 18px 40px rgba(40, 80, 120, 0.18);
  }
  .screen--map { left: 60px; }
  .screen--menu { left: 445px; }
  .screen--list { left: 830px; }
  .screen__inner { position: relative; width: 100%; height: 100%; border-radius: 32px; overflow: hidden; }

  .map-area {
    position: absolute; inset: 0;
    background: linear-gradient(160deg, var(--map-light) 0%, var(--map-mid) 55%, var(--map-light) 100%);
  }
  .map-pin { position: absolute; width: 42px; height: 52px; filter: drop-shadow(0 0 8px rgba(21,116,180,0.5)); }

  .nav-bar {
    position: absolute; left: 16px; right: 16px; bottom: 18px; height: 72px;
    background: var(--brand-blue); border-radius: 22px;
    display: flex; align-items: center; justify-content: space-around;
    box-shadow: 0 0 18px rgba(21,116,180,0.45);
  }
  .nav-bar__tab--active {
    width: 54px; height: 54px; border-radius: 16px; background: #fff;
    display: flex; align-items: center; justify-content: center;
  }

  .overlay {
    position: absolute; left: 0; right: 0; top: 70px; bottom: 0;
    background: var(--overlay-blue); border-radius: 46px 46px 32px 32px;
    backdrop-filter: blur(6px);
  }

  .wordmark { display: flex; align-items: center; gap: 10px; }
  .wordmark__dot { width: 26px; height: 26px; border-radius: 50%; background: var(--brand-blue); }
  .wordmark__name { font-weight: 800; font-size: 30px; letter-spacing: 1px; color: var(--ink); }

  .menu { position: absolute; top: 40px; left: 28px; right: 24px; }
  .menu .wordmark { margin-bottom: 34px; }
  .menu__list { list-style: none; }
  .menu__item {
    display: flex; align-items: center; gap: 14px;
    font-size: 15px; color: var(--ink-soft); padding: 12px 0;
    border-bottom: 1px solid rgba(255,255,255,0.45);
  }
  .menu__item svg { width: 20px; height: 20px; }
  .menu__logout { margin-top: 44px; display: flex; align-items: center; gap: 14px; font-size: 15px; color: var(--ink-soft); }

  .vehicle-list { position: absolute; top: 34px; left: 14px; right: 28px; }
  .vehicle-card {
    position: relative; height: 108px; margin-bottom: 14px;
    background: var(--card-bg); border-radius: 22px; overflow: hidden;
    display: flex; align-items: center; gap: 10px; padding: 0 10px 0 16px;
    box-shadow: 0 6px 14px rgba(30,70,110,0.15);
  }
  .vehicle-card::before { content: ""; position: absolute; left: 0; top: 0; bottom: 0; width: 6px; background: var(--accent); }
  .vehicle-card--green { --accent: var(--accent-green); }
  .vehicle-card--purple { --accent: var(--accent-purple); }
  .vehicle-card--red { --accent: var(--accent-red); }
  .vehicle-card__badge { flex: none; width: 38px; height: 38px; border-radius: 50%; background: #c9d3dc; border: 3px solid #fff; }
  .vehicle-card__info { min-width: 0; }
  .vehicle-card__title { font-size: 11px; font-weight: 700; color: var(--ink); white-space: nowrap; margin-bottom: 2px; }
  .vehicle-card__meta { font-size: 11px; color: var(--ink-soft); line-height: 1.5; white-space: nowrap; }
  .vehicle-card__fav { position: absolute; right: 12px; bottom: 10px; width: 16px; height: 16px; }
  .add-button {
    position: absolute; right: -22px; top: 33px; z-index: 2;
    width: 42px; height: 42px; border-radius: 50%;
    background: var(--brand-blue); color: #fff; font-size: 28px; font-weight: 400;
    line-height: 40px; text-align: center;
    box-shadow: 0 4px 10px rgba(21,116,180,0.35);
  }

  .brand-block { position: absolute; right: 60px; top: 880px; width: 420px; text-align: right; }
  .brand-block .wordmark { justify-content: flex-end; margin-bottom: 26px; }
  .brand-block .wordmark__dot { width: 54px; height: 54px; }
  .brand-block .wordmark__name { font-size: 60px; }
  .brand-block__text { font-size: 15px; font-weight: 700; line-height: 1.3; color: var(--ink); }
</style>
</head>
<body>

<svg width="0" height="0" style="position:absolute">
  <defs>
    <symbol id="icon-pin" viewBox="0 0 42 52">
      <path d="M21 2C10.5 2 3 10 3 20c0 13 18 30 18 30s18-17 18-30C39 10 31.5 2 21 2z" fill="#1574b4" stroke="#fff" stroke-width="3"/>
      <circle cx="21" cy="20" r="7" fill="#fff"/>
    </symbol>
    <symbol id="icon-car" viewBox="0 0 32 32">
      <path d="M6 18l3-8h14l3 8v7h-3v-2H9v2H6z" fill="none" stroke="#1574b4" stroke-width="2" stroke-linejoin="round"/>
      <circle cx="10.5" cy="19.5" r="1.5" fill="#1574b4"/><circle cx="21.5" cy="19.5" r="1.5" fill="#1574b4"/>
    </symbol>
    <symbol id="icon-gear" viewBox="0 0 32 32">
      <circle cx="16" cy="16" r="5" fill="none" stroke="#cfe3f2" stroke-width="2"/>
      <circle cx="16" cy="16" r="10" fill="none" stroke="#cfe3f2" stroke-width="2" stroke-dasharray="4 3"/>
    </symbol>
    <symbol id="icon-chart" viewBox="0 0 32 32">
      <path d="M6 26h20M9 24v-5M14 24v-9M19 24v-7M24 24v-12" stroke="#cfe3f2" stroke-width="2.4" fill="none"/>
    </symbol>
    <symbol id="icon-heart" viewBox="0 0 16 16">
      <path d="M8 14S1.5 9.8 1.5 5.5A3.2 3.2 0 0 1 8 4a3.2 3.2 0 0 1 6.5 1.5C14.5 9.8 8 14 8 14z" fill="#1574b4"/>
    </symbol>
  </defs>
</svg>

<!-- Map screen -->
<section class="screen screen--map" aria-label="Map screen">
  <div class="screen__inner">
    <div class="map-area" role="img" aria-label="Street map of the neighbourhood with tracked vehicles"></div>
    <svg class="map-pin" style="left:70px;top:150px"><use href="#icon-pin"/></svg>
    <svg class="map-pin" style="left:200px;top:240px"><use href="#icon-pin"/></svg>
    <svg class="map-pin" style="left:120px;top:410px"><use href="#icon-pin"/></svg>
    <nav class="nav-bar">
      <span class="nav-bar__tab--active"><svg width="30" height="30"><use href="#icon-car"/></svg></span>
      <svg width="30" height="30"><use href="#icon-gear"/></svg>
      <svg width="30" height="30"><use href="#icon-chart"/></svg>
    </nav>
  </div>
</section>

<!-- Menu screen -->
<section class="screen screen--menu" aria-label="Menu screen">
  <div class="screen__inner">
    <div class="map-area" role="img" aria-label="Street map of the neighbourhood, dimmed"></div>
    <div class="overlay">
      <div class="menu">
        <div class="wordmark"><span class="wordmark__dot"></span><span class="wordmark__name">QUELMO</span></div>
        <ul class="menu__list">
          <li class="menu__item"><svg viewBox="0 0 20 20"><circle cx="10" cy="7" r="4" fill="none" stroke="#1f5f8f" stroke-width="1.6"/><path d="M3 18c1-4 4-5 7-5s6 1 7 5" fill="none" stroke="#1f5f8f" stroke-width="1.6"/></svg>Profile</li>
          <li class="menu__item"><svg viewBox="0 0 20 20"><path d="M4 10a6 6 0 0 1 11-3M16 10a6 6 0 0 1-11 3" fill="none" stroke="#1f5f8f" stroke-width="1.6"/><path d="M15 3v4h-4M5 17v-4h4" fill="none" stroke="#1f5f8f" stroke-width="1.6"/></svg>Subscription</li>
          <li class="menu__item"><svg viewBox="0 0 20 20"><rect x="3" y="4" width="14" height="12" rx="2" fill="none" stroke="#1f5f8f" stroke-width="1.6"/><path d="M8 7.5l5 2.5-5 2.5z" fill="#1f5f8f"/></svg>Tutorials</li>
          <li class="menu__item"><svg viewBox="0 0 20 20"><path d="M4 12V9a6 6 0 0 1 12 0v3" fill="none" stroke="#1f5f8f" stroke-width="1.6"/><rect x="3" y="11" width="3" height="5" rx="1" fill="#1f5f8f"/><rect x="14" y="11" width="3" height="5" rx="1" fill="#1f5f8f"/></svg>Support</li>
          <li class="menu__item"><svg viewBox="0 0 20 20"><path d="M5 14V9a5 5 0 0 1 10 0v5l1.5 2h-13z" fill="none" stroke="#1f5f8f" stroke-width="1.6"/><circle cx="10" cy="17.5" r="1.5" fill="#1f5f8f"/></svg>Alert Settings</li>
        </ul>
        <div class="menu__logout"><svg width="20" height="20" viewBox="0 0 20 20"><path d="M6 5a7 7 0 1 0 8 0" fill="none" stroke="#e0404a" stroke-width="1.8"/><path d="M10 2v8" stroke="#e0404a" stroke-width="1.8"/></svg>Logout</div>
      </div>
    </div>
  </div>
</section>

<!-- Vehicle list screen -->
<section class="screen screen--list" aria-label="Vehicle list screen">
  <div class="screen__inner">
    <div class="map-area" role="img" aria-label="Street map of the neighbourhood, dimmed"></div>
    <div class="overlay">
      <div class="vehicle-list">
        <article class="vehicle-card vehicle-card--green">
          <span class="vehicle-card__badge"></span>
          <div class="vehicle-card__info"><p class="vehicle-card__title">Bravik B150 Black – HST-450</p><p class="vehicle-card__meta">Parked - at School lane<br>Since 2:03 pm</p></div>
          <svg class="vehicle-card__fav"><use href="#icon-heart"/></svg>
        </article>
        <article class="vehicle-card vehicle-card--purple">
          <span class="vehicle-card__badge"></span>
          <div class="vehicle-card__info"><p class="vehicle-card__title">Bravik B150 Black – HST-450</p><p class="vehicle-card__meta">Parked - at School lane<br>Since 2:03 pm</p></div>
          <svg class="vehicle-card__fav"><use href="#icon-heart"/></svg>
        </article>
        <article class="vehicle-card vehicle-card--red">
          <span class="vehicle-card__badge"></span>
          <div class="vehicle-card__info"><p class="vehicle-card__title">Bravik B150 Black – HST-450</p><p class="vehicle-card__meta">Parked - at School lane<br>Since 2:03 pm</p></div>
          <svg class="vehicle-card__fav" viewBox="0 0 16 16"><path d="M8 14S1.5 9.8 1.5 5.5A3.2 3.2 0 0 1 8 4a3.2 3.2 0 0 1 6.5 1.5C14.5 9.8 8 14 8 14z" fill="none" stroke="#1574b4" stroke-width="1.4"/></svg>
        </article>
        <span class="add-button">+</span>
      </div>
      <nav class="nav-bar">
        <span class="nav-bar__tab--active"><svg width="30" height="30"><use href="#icon-car"/></svg></span>
        <svg width="30" height="30"><use href="#icon-gear"/></svg>
        <svg width="30" height="30"><use href="#icon-chart"/></svg>
      </nav>
    </div>
  </div>
</section>

<!-- Brand block -->
<aside class="brand-block">
  <div class="wordmark"><span class="wordmark__dot"></span><span class="wordmark__name">QUELMO</span></div>
  <p class="brand-block__text">This is a GPS tracker app will be used by<br>parents to track family cars or a small<br>business with a fleet of vehicles. Its main<br>benefits are family safety and fleet tracking.</p>
</aside>

</body>
</html>
```